Animal Eye Clinic needs a Business card

We are a new veterinary ophthalmology practice (Tessaly Animal Eye Care) and we need a business card designed. We only see animal eyes - we are not a regular veterinary clinic. We already have a logo. We are looking for a professional, good looking business card to hand out to our clients. We are looking for something simple but professional and contemporary. Our logo is likely the only picture/graphic that needs to be on the card.
Updates

Contact Information for Business Card

Marisol Dunkley, BSc, DVM, MSc, DipACVO
Veterinary Ophthalmologist

Phone: 250.418.3097
Email: tessalyanimaleyecare@mailbrook.net
Website: tessalyanimaleyecare.net
Address: 1840 Pellworth Rd
Kelowna, BC, V4T 8M3

Colors

Designer to choose colors to be used in the design.

Requirements
Must have
• Our logo (attached)

```html
<!DOCTYPE html>
<html lang="en">
<head>
<meta charset="utf-8">
<title>Tessaly Animal Eye Care – Business Card</title>
<link rel="stylesheet" href="https://fonts.googleapis.com/css2?family=Open+Sans:ital,wght@0,400;0,800;1,400&display=swap">
<style>
  :root {
    --page-bg: #ebf4f7;
    --card-bg: #ffffff;
    --teal: #3a9aab;
    --ink: #4a4a4a;
  }
  * { margin: 0; padding: 0; box-sizing: border-box; }
  html, body {
    width: 1200px; height: 900px; overflow: hidden;
    background: var(--page-bg);
    font-family: "Open Sans", Arial, sans-serif;
  }
  .card {
    position: absolute;
    left: 152px; top: 160px;
    width: 896px; height: 580px;
    background: var(--card-bg);
    border: 8px solid var(--teal);
    overflow: hidden;
  }
  .identity { position: absolute; left: 32px; top: 30px; }
  .identity__name {
    font-weight: 800; font-size: 45px; line-height: 1.05;
    color: var(--teal); letter-spacing: 0.3px;
  }
  .identity__credentials {
    font-weight: 800; font-size: 29px; line-height: 1.2;
    color: var(--teal);
  }
  .identity__title {
    margin-top: 4px;
    font-style: italic; font-size: 23px;
    color: var(--ink);
  }
  .contact {
    position: absolute; left: 34px; top: 435px;
    list-style: none;
  }
  .contact__item {
    display: flex; align-items: center;
    height: 27px;
    font-size: 19px; color: var(--ink);
  }
  .contact__icon {
    width: 15px; height: 15px; margin-right: 10px;
    fill: var(--teal); flex: none;
  }
  .brand {
    position: absolute; right: 40px; top: 50%;
    transform: translateY(-50%);
    display: flex; align-items: center; gap: 16px;
  }
  .brand__dot {
    width: 56px; height: 56px; border-radius: 50%;
    background: var(--teal); flex: none;
  }
  .brand__name {
    font-weight: 800; font-size: 30px; line-height: 1.15;
    color: var(--teal);
  }
</style>
</head>
<body>
  <main class="card">
    <header class="identity">
      <h1 class="identity__name">Marisol Dunkley,</h1>
      <p class="identity__credentials">BSc, DVM, MSc, DipACVO</p>
      <p class="identity__title">Veterinary Ophthalmologist</p>
    </header>

    <div class="brand">
      <span class="brand__dot"></span>
      <p class="brand__name">Tessaly<br>Animal Eye Care</p>
    </div>

    <ul class="contact">
      <li class="contact__item">
        <svg class="contact__icon" viewBox="0 0 24 24" aria-hidden="true"><path d="M6.6 10.8a15 15 0 0 0 6.6 6.6l2.2-2.2a1 1 0 0 1 1-.25 11.4 11.4 0 0 0 3.6.57 1 1 0 0 1 1 1V20a1 1 0 0 1-1 1A17 17 0 0 1 3 4a1 1 0 0 1 1-1h3.5a1 1 0 0 1 1 1c0 1.25.2 2.45.57 3.57a1 1 0 0 1-.25 1z"/></svg>
        (250) 418-3097
      </li>
      <li class="contact__item">
        <svg class="contact__icon" viewBox="0 0 24 24" aria-hidden="true"><path d="M2 5h20v14H2z M3 6l9 7 9-7" stroke="#fff" stroke-width="1.5"/></svg>
        tessalyanimaleyecare.net
      </li>
      <li class="contact__item">
        <svg class="contact__icon" viewBox="0 0 24 24" aria-hidden="true" fill="none" stroke="currentColor" style="color:var(--teal)"><circle cx="12" cy="12" r="9.5" stroke-width="1.4"/><ellipse cx="12" cy="12" rx="4.5" ry="9.5" stroke-width="1.2"/><path d="M2.5 12h19M4 7h16M4 17h16" stroke-width="1.2"/></svg>
        tessalyanimaleyecare@mailbrook.net
      </li>
      <li class="contact__item">
        <svg class="contact__icon" viewBox="0 0 24 24" aria-hidden="true"><path d="M12 2a7 7 0 0 0-7 7c0 5 7 13 7 13s7-8 7-13a7 7 0 0 0-7-7zm0 9.5a2.5 2.5 0 1 1 0-5 2.5 2.5 0 0 1 0 5z"/></svg>
        1840 Pellworth Rd Kelowna, BC, V4T 8M3
      </li>
    </ul>
  </main>
</body>
</html>
```